Website Design - for Energy Efficiency company - large corporate feel

Hi there,
Thanks for checking out this project!
We're a UK based energy efficiency business. We arrange for energy efficient systems to be fitted in people's houses (i.e. efficient boilers, solar panels etc.) However, we do not install them ourselves as we have accredited installers who install on our behalf. Therefore the website should appeal to these businesses and have a very professional corporate feel. The final design should communicate that we are a financially safe large corporation.
Our existing website should not be used for inspiration as the style and content are very outdated (it was from a time when were installers - which we no longer are).
The new website design should use the greens from our logo, however I don't want the site saturated in this colour.
I'm really open to your chosen layout and therefore I'm not a huge fan of including links to websites I like - as I don't want to limit your own creativity. However, I would like it to look corporate (but not too boring and unimaginative).
So here's a few links to websites that I feel give a feel of financially safe / large corporate etc. Although you certainly don't have to design with this style / layout in mind:
http://www.brelvanhub.org.uk/advice
http://www.tolvenrise.co.uk/
http://www.qpwd.org.uk/
http://www.wendrowkeyplot.co.uk/
http://www.ruvasto.co.uk/ (very bad design but looks corporate)
http://www.pellarwatt.org.uk/
http://www.vq.co.uk/ (looks corporate but too busy and boring)
http://www.quellisto.co.uk/business/index.htm
http://www.dormavel.com/
https://www.ostrevan.com/en/index.html
The site is for 4 different audiences:
Consumers | Businesses | Public Sector | Installers
Therefore, it's important that there is some form of way of splitting the site up into these sections (almost like 4 websites in 1). Each section will then have the navigation menu with 7 links.
I've attached our logo (company-logo.jpg) and another logo design we have to display inline with regulations (blue-pact-logo.jpg).
Happy designing, and thank you!

```html
<!DOCTYPE html>
<html lang="en">
<head>
<meta charset="utf-8">
<title>Verdalo Energy</title>
<link href="https://fonts.googleapis.com/css2?family=Lato:wght@300;400;700;900&family=Roboto+Slab:wght@700&display=swap" rel="stylesheet">
<style>
:root{
  --green:#5c9a1e;
  --green-bright:#7cbd2c;
  --green-dark:#4f8a19;
  --blue:#1b6a8e;
  --blue-dark:#0f3f57;
  --ink:#222;
  --grey:#555;
  --light:#efefef;
  --footer:#2d2d2d;
  --footer-text:#9a9a9a;
}
*{margin:0;padding:0;box-sizing:border-box}
html,body{width:1200px;height:1128px;overflow:hidden;background:#fff}
body{font-family:'Lato',sans-serif;color:var(--ink);position:relative}
a{color:inherit;text-decoration:none}
.abs{position:absolute}

/* header */
.brand{left:202px;top:30px;display:flex;align-items:center;gap:10px}
.brand-dot{width:40px;height:40px;border-radius:50%;background:var(--green)}
.brand-name{font-size:32px;font-weight:700;color:var(--green);letter-spacing:-0.5px}
.search{left:803px;top:21px;width:198px;height:28px;border:1px solid #ddd;border-radius:14px;font-size:10px;color:#aaa;padding:8px 0 0 19px}
.search-btn{position:absolute;right:2px;top:2px;width:22px;height:22px;border-radius:50%;background:var(--green-bright)}
.nav{left:516px;top:66px;display:flex;gap:0;font-size:14px;color:#555}
.nav a{padding:3px 8px 0;height:32px;position:relative}
.nav a.active{color:#444}
.nav a.active::after{content:"";position:absolute;left:0;right:0;bottom:0;height:4px;background:var(--green-bright)}

/* hero */
.hero{left:0;top:99px;width:1200px;height:354px;background:var(--light)}
.hero-scene{position:absolute;left:101px;top:0;width:936px;height:354px;background:linear-gradient(180deg,#5f9ed8 0%,#a9cbe8 45%,#dfe7ee 75%,#8a9099 100%)}
.hero-box{left:200px;top:186px;width:450px;height:106px;background:var(--green-bright);border-right:10px solid var(--green-dark);padding:14px 0 0 20px;color:#fff}
.hero-title{font-family:'Roboto Slab',serif;font-size:31px;letter-spacing:-1.2px;line-height:1.1}
.hero-sub{font-size:19px;font-weight:300;line-height:21px;letter-spacing:-0.6px;margin-top:6px}
.btn{display:flex;align-items:center;gap:8px;background:var(--blue);color:#fff;font-weight:700;letter-spacing:-0.7px;border-right:8px solid var(--blue-dark)}
.hero-btn{left:202px;top:294px;width:145px;height:38px;font-size:19px;padding-left:14px}
.dots{left:201px;top:340px;display:flex;gap:2px}
.dots span{width:9px;height:9px;border-radius:50%;background:#2b2b2b}
.dots span:first-child{background:var(--green-bright)}

/* audiences */
.audience{top:494px;width:150px;text-align:center}
.audience-icon{width:100px;height:100px;border-radius:50%;background:var(--blue);margin:0 auto;display:flex;align-items:center;justify-content:center}
.audience h3{font-size:16.5px;font-weight:900;color:var(--green);letter-spacing:-0.8px;margin-top:11px}
.audience p{font-size:9px;line-height:11px;color:#333;margin-top:3px}
.audience a{display:block;margin-top:5px;font-size:10.5px;font-weight:900;color:var(--blue);text-decoration:underline}
.divider{left:190px;top:712px;width:815px;height:1px;background:linear-gradient(90deg,transparent,#ddd 15%,#ddd 85%,transparent)}

/* news */
.section-title{font-size:25px;font-weight:900;color:var(--green);letter-spacing:-1.8px}
.arrows{left:574px;top:752px;display:flex;gap:2px}
.arrows span{width:21px;height:20px;background:var(--blue);display:flex;align-items:center;justify-content:center}
.news-thumb{left:202px;top:789px;width:120px;height:61px;background:#263638;display:flex;padding:3px}
.news-photo{width:56px;height:55px;background:linear-gradient(135deg,#dfe6ea,#8e9ba3)}
.news-date{flex:1;text-align:center;color:#fff;padding-top:6px}
.news-date b{display:block;font-size:24px;font-weight:900;line-height:22px}
.news-date span{font-size:11px}
.news-head{left:328px;top:789px;font-size:13px;font-weight:700;letter-spacing:-0.3px}
.news-text{left:328px;top:809px;width:300px;font-size:10.5px;line-height:13.6px;color:#444}
.news-author{left:202px;top:861px;font-size:10.5px;line-height:13px}
.news-author b{font-weight:900}
.vline{left:643px;top:750px;width:1px;height:140px;background:#e2e2e2}

/* why */
.why-sub{left:661px;top:772px;font-size:18px;font-weight:700;letter-spacing:-0.9px}
.why-list{left:660px;top:799px;list-style:none;font-size:14px;font-weight:300;color:#333;letter-spacing:-0.3px}
.why-list li{display:flex;align-items:center;gap:8px;height:20.5px}
.tick{width:12px;height:12px;border-radius:50%;background:var(--green-bright);flex:none}
.why-btn{left:660px;top:864px;width:92px;height:23px;font-size:12px;padding-left:9px;border-right-width:5px}

/* footer */
.footer{left:0;top:936px;width:1200px;height:192px;background:var(--footer);color:var(--footer-text)}
.f-col{position:absolute;top:22px}
.f-col h4{font-size:19px;font-weight:400;color:#fff;margin-bottom:8px}
.f-about h4{font-weight:900;letter-spacing:-1px}
.f-about p{font-size:12px;line-height:17px;width:265px;font-weight:300;color:#aaa}
.f-col ul{list-style:none;font-size:10.5px;line-height:15.8px;font-weight:300;color:#aaa}
.f-contact ul{line-height:19px}
.f-brand{left:202px;top:130px;display:flex;align-items:center;gap:8px}
.f-brand .brand-dot{width:32px;height:32px;background:#fff}
.f-brand .brand-name{color:#fff;font-size:26px}
.social{display:flex;gap:4px;margin-top:10px}
.social span{width:24px;height:24px;border-radius:50%;background:#fff}
.copyright{right:197px;top:161px;font-size:12.5px;font-weight:300;color:#8a8a8a}
</style>
</head>
<body>

<header>
  <div class="abs brand"><span class="brand-dot"></span><span class="brand-name">Verdalo Energy</span></div>
  <div class="abs search">Search Key Words<span class="search-btn"></span></div>
  <nav class="abs nav">
    <a class="active" href="#">Home</a><a href="#">Insulation</a><a href="#">Heating</a><a href="#">Solar</a><a href="#">Funding</a><a href="#">Help &amp; Advice</a><a href="#">Contact Us</a>
  </nav>
</header>

<section class="abs hero">
  <div class="hero-scene" role="img" aria-label="Sky with wind turbines and solar panels beside a smiling businessman with folded arms"></div>
</section>
<div class="abs hero-box">
  <h1 class="hero-title">Power Your Home For Free</h1>
  <p class="hero-sub">Generate Electricity And Income For Your Home<br>With Solar Panels</p>
</div>
<a class="abs btn hero-btn" href="#">Read More
  <svg width="22" height="22" viewBox="0 0 22 22"><circle cx="11" cy="11" r="9.5" fill="none" stroke="#fff" stroke-width="2"/><path d="M6 11h9M11 7l4 4-4 4" fill="none" stroke="#fff" stroke-width="2"/></svg></a>
<div class="abs dots"><span></span><span></span><span></span><span></span><span></span><span></span></div>

<section>
  <div class="abs audience" style="left:309px">
    <div class="audience-icon"><svg width="60" height="60" viewBox="0 0 60 60" fill="#fff"><circle cx="16" cy="18" r="6"/><circle cx="44" cy="18" r="6"/><circle cx="30" cy="14" r="8"/><path d="M6 44v-12q0-6 10-6 4 0 6 1v17zM54 44v-12q0-6-10-6-4 0-6 1v17z"/><path d="M17 50v-17q0-8 13-8t13 8v17z"/></svg></div>
    <h3>CONSUMERS</h3>
    <p>Lorem Ipsum Dolor Sit Amet,<br>Consectetuer Adipiscing Elit,<br>Sed Diam Nonummy Nibh.</p>
    <a href="#">READ MORE</a>
  </div>
  <div class="abs audience" style="left:451px">
    <div class="audience-icon"><svg width="66" height="50" viewBox="0 0 66 50" fill="#fff"><path d="M24 8V4h18v4h-3V7H27v1z"/><rect x="2" y="9" width="62" height="38" rx="5"/><rect x="30" y="25" width="6" height="5" fill="#1b6a8e"/><rect x="2" y="26" width="62" height="1.5" fill="#1b6a8e"/></svg></div>
    <h3>BUSINESSES</h3>
    <p>Lorem Ipsum Dolor Sit Amet,<br>Consectetuer Adipiscing Elit,<br>Sed Diam Nonummy Nibh.</p>
    <a href="#">READ MORE</a>
  </div>
  <div class="abs audience" style="left:593px">
    <div class="audience-icon"><svg width="66" height="74" viewBox="0 0 66 74" fill="#fff"><circle cx="33" cy="10" r="7"/><path d="M22 32q0-12 11-12t11 12z"/><path d="M26 34h14v18h8L33 70 18 52h8z"/><path d="M2 44l12-9v5h10v8H14v5zM64 44l-12-9v5H42v8h10v5z"/></svg></div>
    <h3>PUBLIC SECTOR</h3>
    <p>Lorem Ipsum Dolor Sit Amet,<br>Consectetuer Adipiscing Elit,<br>Sed Diam Nonummy Nibh.</p>
    <a href="#">READ MORE</a>
  </div>
  <div class="abs audience" style="left:737px">
    <div class="audience-icon"><svg width="64" height="64" viewBox="0 0 64 64" fill="none" stroke="#fff" stroke-width="8" stroke-linecap="round"><path d="M12 8l22 22"/><path d="M54 12L18 50"/><circle cx="14" cy="53" r="6" stroke-width="5"/><path d="M38 42l14 14" stroke-width="10"/></svg></div>
    <h3>INSTALLERS</h3>
    <p>Lorem Ipsum Dolor Sit Amet,<br>Consectetuer Adipiscing Elit,<br>Sed Diam Nonummy Nibh.</p>
    <a href="#">READ MORE</a>
  </div>
</section>
<div class="abs divider"></div>

<section>
  <h2 class="abs section-title" style="left:203px;top:744px">LATEST NEWS.</h2>
  <div class="abs arrows">
    <span><svg width="10" height="12" viewBox="0 0 10 12"><path d="M7 1L2 6l5 5" fill="none" stroke="#fff" stroke-width="2.5"/></svg></span>
    <span><svg width="10" height="12" viewBox="0 0 10 12"><path d="M3 1l5 5-5 5" fill="none" stroke="#fff" stroke-width="2.5"/></svg></span>
  </div>
  <div class="abs news-thumb">
    <div class="news-photo" role="img" aria-label="Business team meeting around a table"></div>
    <div class="news-date"><b>28</b><span>SEPT</span></div>
  </div>
  <h3 class="abs news-head">LOREM IPSUM DOLOR SIT AMET CONSECTETUER</h3>
  <p class="abs news-text">Adipiscing Elit, Sed Diam Nonummy Nibh Euismod Tincidunt Ut Laoreet Dolore Magna Aliquam Erat Volutpat. Ut Wisi Enim Ad Minim Veniam, Quis Nostrud.</p>
  <p class="abs news-author"><b>GUIHMOD TINCSFUFT</b><br>ASYIOD GPIDUNT</p>
</section>
<div class="abs vline"></div>

<section>
  <h2 class="abs section-title" style="left:661px;top:746px">WHY CHOOSE US.</h2>
  <p class="abs why-sub">Founders and Entrepreneurs</p>
  <ul class="abs why-list">
    <li><span class="tick"></span>Save Time And Grow Your Business FasterGrow Business</li>
    <li><span class="tick"></span>Comply With Your Reporting Obligations Resources.</li>
    <li><span class="tick"></span>Free Platform, Resources And Guidance Notes</li>
  </ul>
  <a class="abs btn why-btn" href="#">Read More
    <svg width="14" height="14" viewBox="0 0 22 22"><circle cx="11" cy="11" r="9.5" fill="none" stroke="#fff" stroke-width="2.5"/><path d="M6 11h9M11 7l4 4-4 4" fill="none" stroke="#fff" stroke-width="2.5"/></svg></a>
</section>

<footer class="abs footer">
  <div class="f-col f-about" style="left:203px">
    <h4>About Verdalo Energy</h4>
    <p>Lorem ipsum dolor sit amet, consectetuer adipiscing elit, sed diam nonummy nibh euismod tincidunt ut laoreet dolore magna aliquam.adipiscing elit, sed diam nonummy.</p>
  </div>
  <div class="abs f-brand"><span class="brand-dot"></span><span class="brand-name">Verdalo Energy</span></div>
  <div class="f-col" style="left:525px">
    <h4>About</h4>
    <ul><li>What we do</li><li>Insights</li><li>Meet the team</li><li>Careers</li><li>Our story</li><li>Media</li></ul>
  </div>
  <div class="f-col" style="left:691px">
    <h4>FAQ</h4>
    <ul><li>Help</li><li>Privacy Policy</li><li>Terms of Service</li><li>Contact Us</li><li>Insights</li><li>Meet the team</li></ul>
  </div>
  <div class="f-col f-contact" style="left:839px">
    <h4>Contact</h4>
    <ul><li>Phone: +44 20 7946 0310</li><li>Telefax: +44 20 7946 0380</li><li>Email: info@verdaloenergy.com</li></ul>
    <div class="social"><span></span><span></span><span></span></div>
  </div>
  <p class="abs copyright">Copyright © 2013 Verdalo Energy All Rights Reserved.</p>
</footer>

</body>
</html>
```